We need a card design for our company Harbor Lantern Partners. Our goal is to save people money on their disposal services. For this post card please put our logo in it. Please use these colors Pantone 576c and 418c or green and grey. We are giving you as the designer the opportunity to be creative with any other images. We are looking to have a fun eye catching postcard.
Please write:
Think you are stuck with your trash bill? Think again
We cut your neighbors disposal cost by 40%.

Please put down our information also,
Contact us
800.514.7262
melinda@plumcrest782.com
plumcrest782.com

```html
<!DOCTYPE html>
<html lang="en">
<head>
<meta charset="utf-8">
<title>Harbor Lantern Partners Postcard</title>
<link rel="stylesheet" href="https://fonts.googleapis.com/css2?family=Source+Sans+3:wght@400;600;700&display=swap">
<style>
  :root {
    --paper: #ffffff;
    --frame: #3a3a3a;
    --sun: #fff87a;
    --ink: #111111;
    --brand-grey: #5b5f63;
    --brand-green: #5a8f3a;
    --can-tone: #eef0a6;
    --pig-tone: #f4b3a0;
  }
  html, body {
    margin: 0;
    padding: 0;
    overflow: hidden;
    background: var(--paper);
  }
  .postcard {
    position: relative;
    width: 1200px;
    height: 816px;
    background: var(--paper);
    font-family: "Source Sans 3", "Myriad Pro", Arial, sans-serif;
    color: var(--ink);
    overflow: hidden;
  }
  .postcard__frame {
    position: absolute;
    left: 24px;
    top: 24px;
    width: 1152px;
    height: 766px;
    border: 1.5px solid var(--frame);
    box-sizing: border-box;
  }
  .postcard__offer-panel {
    position: absolute;
    left: 622px;
    top: 25px;
    width: 553px;
    height: 764px;
    background: var(--sun);
  }
  .teaser {
    position: absolute;
    left: 70px;
    top: 64px;
    width: 446px;
    margin: 0;
    text-align: center;
    font-weight: 600;
    font-size: 28px;
    line-height: 36px;
  }
  .art-trash-can {
    position: absolute;
    left: 80px;
    top: 196px;
    width: 345px;
    height: 510px;
    border-radius: 40px 40px 30px 30px;
    background: linear-gradient(180deg, #d9dbdc 0%, var(--can-tone) 40%, #f3f4c4 100%);
  }
  .art-piggy-bank {
    position: absolute;
    left: 725px;
    top: 400px;
    width: 355px;
    height: 300px;
    border-radius: 48% 52% 44% 50%;
    background: radial-gradient(circle at 50% 55%, var(--pig-tone) 0%, #f8d49a 100%);
  }
  .headline {
    position: absolute;
    left: 640px;
    top: 68px;
    width: 520px;
    margin: 0;
    text-align: center;
    font-weight: 700;
    font-size: 72px;
    line-height: 85px;
    letter-spacing: -0.5px;
  }
  .brand {
    position: absolute;
    left: 440px;
    top: 318px;
    width: 300px;
    text-align: center;
  }
  .brand__mark {
    display: block;
    width: 70px;
    height: 70px;
    margin: 0 auto 18px;
    background: var(--brand-green);
  }
  .brand__name {
    margin: 0;
    font-weight: 600;
    font-size: 40px;
    line-height: 44px;
    color: var(--brand-grey);
  }
  .contact {
    position: absolute;
    left: 412px;
    top: 596px;
    width: 368px;
    margin: 0;
    text-align: center;
    font-style: normal;
    font-size: 27px;
    line-height: 38px;
  }
  .contact__title {
    font-weight: 700;
  }
</style>
</head>
<body>
  <main class="postcard">
    <div class="postcard__offer-panel"></div>
    <div class="postcard__frame"></div>

    <p class="teaser">Think you are stuck with your<br>trash bill/bin?<br>Think again</p>

    <div class="art-trash-can" role="img" aria-label="Cartoon of a grumpy overflowing trash can raising a finger"></div>

    <h1 class="headline">We cut your<br>neighbor’s<br>disposal cost<br>by 40%.</h1>

    <div class="art-piggy-bank" role="img" aria-label="Red line drawing of a hand dropping a coin into a smiling piggy bank"></div>

    <div class="brand">
      <span class="brand__mark"></span>
      <p class="brand__name">Harbor Lantern<br>Partners</p>
    </div>

    <address class="contact">
      <span class="contact__title">Contact us:</span><br>
      800.514.7262<br>
      melinda@plumcrest782.com<br>
      plumcrest782.com
    </address>
  </main>
</body>
</html>
```